Independent Consultant needs jazzy website for official company launch!

I need a simple (I think), 4-6 page wordpress design for a hosted wordpress site. I have a new logo for the company (it's a puzzle piece), and business cards but no other marketing materials developed yet.

The main features of the website are Services Offered and How Clients Use Us pages and a Resources section.

Section structure:
About us
Services Offered
How Clients Use Us
Blog
Resources

Blog items
I will use keywords and comments, categories and tags.
Images will be used and should be clickable to see larger picture.

Nature of business:
-Velbor Group, Inc. is a start-up independent management consulting firm based in the Twin Cities, MN but with affiliates in other US locations. We specialize in brain-based, research-based organization development, learning, and coaching services.
- my background: organization behavior, neuroscience, training design and delivery, change management, management coaching, facilitation

Favourite colors:
- citron green
-orange
-grey
-blues - not turqoise or teal

Updates
•Instead of creating a bunch of custom css/html, i would like the final design to be based on one of these themes (these are my favorites):
Quillwhistle, Bramblet, UPelk, Lovisture, Odask, Fenwisha, Marlowbe, Glimbers, Vusko, Halberquint)

Target Market(s)
business owners, executives, mid-upper level managers in private and public sector companies

Examples of sites I kind of like:
http://www.trosnik-example.com
Updates

                                        I am posting a scanned front and back business card to give you an idea of the style I've used so far.  Thank you!

Industry/Entity Type

Management Consulting

Requirements
Must have
• resources page must be set up like a small store - i'll want to sell books, training materials from this site

also would like to build a mailing list over time so that i can send a periodic newsletter to visitors
Should not have
• difficult updates or require me to hire someone to make simple content edits - i'd like to do that on my own

don't want a lot of 'generic' people in photos on my site - would rather have a few real photos included or some visuals of symbols or objects that relate to the work provided

like bold, modern look but not too cutesy or young looking

```html
<!DOCTYPE html>
<html lang="en">
<head>
<meta charset="utf-8">
<title>Velbor Group, Inc</title>
<link href="https://fonts.googleapis.com/css2?family=Source+Sans+3:wght@400;600&family=Questrial&display=swap" rel="stylesheet">
<style>
:root{
  --bg:#ededef;
  --paper:#ffffff;
  --green:#8cb32c;
  --green-dark:#6fa533;
  --green-deep:#4e8b1a;
  --green-light:#a6cd46;
  --text:#3d3d3d;
  --muted:#555;
  --line:#cfcfcf;
}
*{box-sizing:border-box;margin:0;padding:0}
html,body{width:1200px;height:1103px;overflow:hidden;background:var(--bg);font-family:"Source Sans 3",sans-serif;color:var(--text)}
.page{position:absolute;left:152px;top:5px;width:895px;height:993px;background:var(--paper);border:1px solid #e0e0e0}
.abs{position:absolute}
/* header */
.brand{left:163px;top:22px;display:flex;align-items:flex-start;gap:10px}
.brand-mark{width:66px;height:66px;background:var(--green);margin-top:0}
.brand-name{font-size:31px;color:var(--green);font-weight:400;line-height:1;margin-top:0}
.brand-tag{left:244px;top:54px;font-size:14px;color:var(--green)}
.search{left:877px;top:28px;width:157px;height:30px;border:1px solid #c9d9a3;border-radius:15px;box-shadow:2px 2px 3px rgba(0,0,0,.12);background:#fff}
.search span{position:absolute;left:14px;top:6px;font-size:12px;color:#8a9b6a}
.search-btn{position:absolute;right:6px;top:5px;width:28px;height:19px;border-radius:9px;background:var(--green-dark)}
/* nav */
.nav{left:164px;top:91px;width:869px;height:33px;display:flex;background:linear-gradient(#9cc23a,#7faa28 60%,#8fb82f)}
.nav a{flex:none;color:#fff;text-decoration:none;font-size:12px;text-transform:uppercase;display:flex;align-items:center;justify-content:center;border-right:1px solid rgba(255,255,255,.35);text-shadow:0 1px 1px rgba(0,0,0,.25)}
.nav a:last-child{border-right:none}
/* hero */
.hero{left:164px;top:124px;width:869px;height:222px;background:linear-gradient(90deg,#e9e7e2 0%,#b89a82 25%,#7a5a46 45%,#c9a48a 62%,#a98b78 80%,#d6d2cc 100%);box-shadow:0 6px 8px rgba(0,0,0,.18)}
.hero-line{left:750px;top:246px;font-size:30px;line-height:37px;color:#fff;font-weight:400;text-shadow:0 1px 3px rgba(0,0,0,.35)}
.hero-arrow{top:136px;width:34px;height:34px;border-radius:50%;background:#fff;box-shadow:0 1px 3px rgba(0,0,0,.3)}
/* welcome */
.welcome-band{left:164px;top:346px;width:869px;height:215px;background:linear-gradient(90deg,#fff 0%,#f2f2f2 40%,#ececec 100%);border-radius:0 0 6px 6px}
.welcome-title{left:185px;top:363px;font-family:"Questrial",sans-serif;font-size:18px;color:#222;width:509px;padding-bottom:4px;border-bottom:1px solid var(--line)}
.welcome-copy{left:185px;top:401px;width:515px;font-size:12px;line-height:17.5px;color:var(--muted)}
.welcome-copy p{margin-bottom:11px}
.news{left:723px;top:371px;width:295px;height:174px;background:var(--green-dark);border-radius:6px;color:#fff}
.news h3{position:absolute;left:14px;top:12px;font-family:"Questrial",sans-serif;font-weight:400;font-size:18px}
.news-list{position:absolute;left:14px;top:38px;width:272px;list-style:none;border-top:1px solid rgba(255,255,255,.4)}
.news-list li{position:relative;padding:9px 0 5px 35px;font-size:12px;line-height:17.5px;border-bottom:1px solid rgba(255,255,255,.4)}
.news-list li:last-child{border-bottom:none}
.news-list li::before{content:"";position:absolute;left:11px;top:14px;width:7px;height:7px;border-radius:50%;background:#fff}
.news-date{color:#1f2a10}
/* cases */
.cases{left:164px;top:571px;width:869px;height:229px;border:1px solid #c8c8c8;border-radius:6px;background:#fff}
.cases-title{left:185px;top:584px;font-family:"Questrial",sans-serif;font-size:17.5px;color:var(--green-deep)}
.case-photo{top:613px;width:216px;height:99px;border:1px solid #cfcfcf;padding:4px;background:#fff}
.case-photo div{width:100%;height:100%}
.case-caption{top:720px;font-family:"Questrial",sans-serif;font-size:15px;line-height:19px;color:#222}
.more{display:inline-block;height:20px;padding:0 5px;font-size:12px;line-height:20px;color:#1c2a05;background:linear-gradient(#a4d04a,#6ea72b);border:1px solid #8bbd3a}
.case-more{top:767px}
.sep{top:611px;height:178px;border-left:1px dotted #555}
/* services */
.svc-photo{left:164px;top:822px;width:143px;height:141px;border-radius:6px;background:linear-gradient(135deg,#d8d6d0,#efece6 45%,#c5b3a2 75%,#e8e6e2)}
.svc-title{left:326px;top:825px;font-family:"Questrial",sans-serif;font-size:17.5px;color:var(--green-deep)}
.svc-copy{left:327px;top:854px;width:410px;font-size:12px;line-height:20px;color:var(--muted)}
.svc-more{left:328px;top:945px}
.cta{left:794px;width:243px;height:79px;border-radius:6px;background:linear-gradient(135deg,#8dc43a,#a9d257 60%,#7fb536);box-shadow:2px 3px 4px rgba(0,0,0,.2);color:#fff;overflow:hidden}
.cta::after{content:"";position:absolute;right:-40px;top:-10px;width:190px;height:130px;border-radius:50%;background:rgba(255,255,255,.12)}
.cta h3{position:absolute;left:21px;top:16px;font-weight:400;font-size:23px;text-transform:uppercase;letter-spacing:-.3px}
.cta span{position:absolute;left:21px;top:50px;font-size:12.5px}
/* footer */
.footer-nav{left:0;top:1030px;width:1200px;text-align:center;font-size:11px;color:#111}
.footer-nav a{color:#111;text-decoration:none;padding:0 6px}
.copyright{left:0;top:1051px;width:1200px;text-align:center;font-size:11px;color:#111}
</style>
</head>
<body>
<div class="page"></div>

<header>
  <div class="abs brand"><div class="brand-mark"></div><div class="brand-name">Velbor Group, Inc</div></div>
  <div class="abs brand-tag">Helping People and organizations thrive!</div>
  <div class="abs search"><span>Search</span><div class="search-btn">
    <svg width="28" height="19" viewBox="0 0 28 19"><circle cx="15.5" cy="8" r="3.5" fill="none" stroke="#fff" stroke-width="1.8"/><line x1="13" y1="10.5" x2="10" y2="13.5" stroke="#fff" stroke-width="2.2" stroke-linecap="round"/></svg>
  </div></div>
  <nav class="abs nav">
    <a href="#" style="width:137px">Home</a>
    <a href="#" style="width:136px">About Us</a>
    <a href="#" style="width:151px">Services Offered</a>
    <a href="#" style="width:146px">How Clients Use Us</a>
    <a href="#" style="width:149px">Blog</a>
    <a href="#" style="width:150px">Resources</a>
  </nav>
</header>

<section>
  <div class="abs hero" role="img" aria-label="Banner photo of smiling colleagues seated in a row"></div>
  <div class="abs hero-line">helping People and<br>Organizations thrive!</div>
  <div class="abs hero-arrow" style="left:943px"><svg width="34" height="34" viewBox="0 0 34 34"><path d="M19 11l-6 6 6 6" fill="none" stroke="#111" stroke-width="2.6"/></svg></div>
  <div class="abs hero-arrow" style="left:982px"><svg width="34" height="34" viewBox="0 0 34 34"><path d="M15 11l6 6-6 6" fill="none" stroke="#111" stroke-width="2.6"/></svg></div>
</section>

<section>
  <div class="abs welcome-band"></div>
  <h2 class="abs welcome-title" style="font-weight:400">Welcome to Our Site</h2>
  <div class="abs welcome-copy">
    <p>Velbor Group, Inc. provides research-based management consulting to help your people and organization thrive!</p>
    <p>Our work is brain-based. What we do and how we do it works with the brain's natural and hard-wired tendencies. No need to spend time and money on Organization Development, Coaching, or Learning consulting that cannot point to supportive research for its impact!</p>
    <p>Our approach is personal, respectful, and collaborative.&nbsp; Our relationships with clients are very important to us; we strive to build enduring partnerships.</p>
  </div>
  <aside class="abs news">
    <h3>News</h3>
    <ul class="news-list">
      <li>Texas School Districts Saving Money Using IPM Technology<br><span class="news-date">30 November, 2011, 11:56 am</span></li>
      <li>Large Capacity RFID Tags: What to Know, What to Expect<br><span class="news-date">22 March, 2010, 11:45 am</span></li>
    </ul>
  </aside>
</section>

<section>
  <div class="abs cases"></div>
  <h2 class="abs cases-title" style="font-weight:400">New Cases</h2>
  <div class="abs case-photo" style="left:186px"><div role="img" aria-label="Photo of a crowd with raised hands in warm orange light" style="background:linear-gradient(135deg,#5a1a08,#d9642a 45%,#7a2a0c 75%,#c4541d)"></div></div>
  <div class="abs case-photo" style="left:472px"><div role="img" aria-label="Photo of a business team in suits posing at an event" style="background:linear-gradient(180deg,#b9a27a,#5e4a3a 45%,#2a2a30 75%,#6e6660)"></div></div>
  <div class="abs case-photo" style="left:779px"><div role="img" aria-label="Photo of a historic red gate building under a pale sky" style="background:linear-gradient(180deg,#c9cdd2 0%,#b7aca2 30%,#8c3328 55%,#a54a3a 75%,#b9aea0 100%)"></div></div>
  <div class="abs sep" style="left:429px"></div>
  <div class="abs sep" style="left:730px"></div>
  <div class="abs case-caption" style="left:186px">Executive coaching –<br>with unorthodox methods</div>
  <div class="abs case-caption" style="left:472px">How to sustain growth in a<br>department store chain</div>
  <div class="abs case-caption" style="left:781px">A European – China joint venture<br>for solar cell production</div>
  <a class="abs more case-more" style="left:187px" href="#">Read More &gt;&gt;</a>
  <a class="abs more case-more" style="left:473px" href="#">Read More &gt;&gt;</a>
  <a class="abs more case-more" style="left:782px" href="#">Read More &gt;&gt;</a>
</section>

<section>
  <div class="abs svc-photo" role="img" aria-label="Photo of a consultant meeting with two clients in a bright office"></div>
  <h2 class="abs svc-title" style="font-weight:400">SERVICES</h2>
  <p class="abs svc-copy">Our work is brain-based. What we do and how we do it works with the brain's natural and hard-wired tendencies. No need to spend time and money on Organization Development, Coaching, or Learning consulting that cannot point to supportive research for its impact!</p>
  <a class="abs more svc-more" href="#">Read More &gt;&gt;</a>
  <a class="abs cta" style="top:812px" href="#"><h3>How Clients Use Us</h3><span>Read More &gt;&gt;</span></a>
  <a class="abs cta" style="top:900px" href="#"><h3>Contact Us</h3><span>Read More &gt;&gt;</span>
    <svg style="position:absolute;left:176px;top:15px;z-index:1" width="48" height="48" viewBox="0 0 48 48"><rect x="2" y="2" width="44" height="44" rx="7" fill="#3a3a3a" stroke="#ddd" stroke-width="2"/><rect x="11" y="11" width="24" height="26" rx="2" fill="#888"/><path d="M18 31l2-6 12-12 4 4-12 12z" fill="#eee"/></svg>
  </a>
</section>

<footer>
  <nav class="abs footer-nav"><a href="#">Home</a>|<a href="#">About us</a>|<a href="#">Services Offered</a>|<a href="#">How Clients Use Us</a>|<a href="#">Blog</a>|<a href="#">Resources</a></nav>
  <div class="abs copyright">Copyrights @2012 All Rigths Reserved</div>
</footer>
</body>
</html>
```